New residential property management company

I have a lot of name recognition in our smaller town due to owning a construction company here. I have now started a residential property management company representing landlords and tenants. Just trying to get my name out there and get some rentals to manage!

```html
<!DOCTYPE html>
<html lang="en">
<head>
<meta charset="utf-8">
<title>Harlow Property Management – Postcard</title>
<link href="https://fonts.googleapis.com/css2?family=Roboto:wght@400;500;700;900&display=swap" rel="stylesheet">
<style>
  :root {
    --brand-blue: #0b56b1;
    --brand-blue-glass: rgba(9, 82, 172, 0.93);
    --ink: #1b1b1b;
    --white: #ffffff;
    --backdrop: #f1f1f1;
    --stamp: #e5e5e5;
    --rule: #c9c9c9;
  }
  * { margin: 0; padding: 0; box-sizing: border-box; }
  html, body {
    width: 1200px; height: 1200px; overflow: hidden;
    background: var(--backdrop);
    font-family: "Roboto", Arial, sans-serif;
  }
  .postcard {
    position: absolute; width: 658px; height: 438px;
    background: var(--white); overflow: hidden;
    box-shadow: 0 2px 6px rgba(0,0,0,0.18);
  }
  .postcard--front { left: 439px; top: 134px; }
  .postcard--back { left: 244px; top: 627px; }

  /* Front */
  .front-photo {
    position: absolute; inset: 0;
    background:
      linear-gradient(180deg, #ffffff 0%, #f3f7fb 18%, #bcd6ef 32%, #e9dca8 50%, #c9b77f 62%, #5f7a3f 78%, #3f6a2a 88%, #c9b9a0 100%);
  }
  .front-panel {
    position: absolute; left: 37px; top: 0; width: 241px; height: 100%;
    background: var(--brand-blue-glass); color: var(--white); text-align: center;
  }
  .headline-need { position: absolute; top: 26px; width: 100%; font-size: 23px; font-weight: 400; }
  .headline-rental { position: absolute; top: 50px; width: 100%; font-size: 46px; font-weight: 900; letter-spacing: -0.5px; line-height: 1; }
  .headline-management { position: absolute; top: 95px; width: 100%; font-size: 24px; font-weight: 700; }
  .help-bubble { position: absolute; left: 49px; top: 129px; width: 143px; height: 44px; }
  .help-bubble span {
    position: absolute; left: 0; top: 0; width: 143px; height: 33px;
    line-height: 33px; font-size: 19px; font-weight: 400;
  }
  .owner-portrait {
    position: absolute; left: 52px; top: 189px; width: 134px; height: 134px;
    border-radius: 50%; border: 3px solid var(--white);
    background: linear-gradient(180deg, #e9ebec 0%, #d9dcde 48%, #8e8b86 52%, #74716c 100%);
  }
  .call-prompt { position: absolute; top: 333px; width: 100%; font-size: 15px; line-height: 18px; }
  .phone-line {
    position: absolute; top: 374px; left: 0; width: 100%;
    display: flex; justify-content: center; align-items: center; gap: 10px;
    font-size: 28px; font-weight: 400;
  }
  .front-brand {
    position: absolute; left: 359px; top: 30px; display: flex; align-items: center; gap: 14px;
    font-size: 50px; font-weight: 500; color: var(--ink); letter-spacing: 2px;
  }
  .brand-dot { width: 44px; height: 44px; border-radius: 50%; background: var(--ink); }

  /* Back */
  .back-panel {
    position: absolute; left: 0; top: 0; width: 348px; height: 100%;
    background: var(--brand-blue); color: var(--white);
  }
  .back-photo {
    position: absolute; left: 0; top: 0; width: 348px; height: 165px;
    background: linear-gradient(180deg, #e7e4df 0%, #7d8591 25%, #8c8672 48%, #4c7a3a 72%, var(--brand-blue) 100%);
  }
  .company-name { position: absolute; left: 34px; top: 152px; font-size: 16px; font-weight: 700; }
  .company-about { position: absolute; left: 34px; top: 175px; width: 290px; font-size: 12.6px; line-height: 15.3px; }
  .cta-box {
    position: absolute; left: 36px; top: 265px; width: 278px; height: 110px;
    border: 1.5px solid var(--white); text-align: center;
  }
  .cta-title { position: absolute; top: 15px; width: 100%; font-size: 16px; font-weight: 400; }
  .cta-title b { font-weight: 700; }
  .cta-sub { position: absolute; top: 37px; width: 100%; font-size: 13px; }
  .cta-box .phone-line { top: 60px; font-size: 28px; }
  .email-line {
    position: absolute; left: 53px; top: 385px; display: flex; align-items: center; gap: 8px;
    font-size: 18px; letter-spacing: 0.2px;
  }
  .back-brand {
    position: absolute; left: 384px; top: 32px; display: flex; align-items: center; gap: 8px;
    font-size: 27px; font-weight: 500; color: var(--ink); letter-spacing: 1px;
  }
  .back-brand .brand-dot { width: 24px; height: 24px; }
  .return-address { position: absolute; left: 384px; top: 78px; font-size: 10.5px; line-height: 13px; color: var(--ink); }
  .stamp-box { position: absolute; left: 569px; top: 30px; width: 61px; height: 61px; background: var(--stamp); }
  .address-rule { position: absolute; left: 386px; width: 241px; height: 1px; background: var(--rule); }
</style>
</head>
<body>

<section class="postcard postcard--front">
  <div class="front-photo" role="img" aria-label="Photo of a yellow two-storey house with porch, white picket fence and tropical garden"></div>
  <div class="front-brand"><span class="brand-dot"></span>HARLOW</div>
  <div class="front-panel">
    <div class="headline-need">NEED</div>
    <div class="headline-rental">RENTAL</div>
    <div class="headline-management">MANAGEMENT?</div>
    <div class="help-bubble">
      <svg width="143" height="44" viewBox="0 0 143 44" fill="none" stroke="#fff" stroke-width="1.5">
        <path d="M1 1 H142 V33 H100 L98 43 L85 33 H1 Z"/>
      </svg>
      <span>We can help!</span>
    </div>
    <div class="owner-portrait" role="img" aria-label="Portrait of the company owner standing in front of a white wall"></div>
    <div class="call-prompt">Just give us a call or<br>send us a text!</div>
    <div class="phone-line">
      <svg width="20" height="28" viewBox="0 0 20 28" fill="none" stroke="#fff" stroke-width="2.2">
        <rect x="1.5" y="1.5" width="13" height="25" rx="2"/>
        <rect x="7" y="6" width="12" height="9" rx="1.5" fill="#fff" stroke="none"/>
        <circle cx="8" cy="22.5" r="1" fill="#fff" stroke="none"/>
      </svg>
      <span>541-555-0182</span>
    </div>
  </div>
</section>

<section class="postcard postcard--back">
  <div class="back-panel">
    <div class="back-photo" role="img" aria-label="Photo of a grey colonial-style house with columned porch and green shrubs"></div>
    <div class="company-name">Harlow Property Management LLC</div>
    <p class="company-about">Is based out of Roseburg, Oregon and our team of experts in residential property management and marketing are looking forward to managing every aspect of your investment property for you and your tenants.</p>
    <div class="cta-box">
      <div class="cta-title">NEED <b>RENTAL MANAGEMENT?</b></div>
      <div class="cta-sub">Just give us a call or send us a text!</div>
      <div class="phone-line">
        <svg width="20" height="28" viewBox="0 0 20 28" fill="none" stroke="#fff" stroke-width="2.2">
          <rect x="1.5" y="1.5" width="13" height="25" rx="2"/>
          <rect x="7" y="6" width="12" height="9" rx="1.5" fill="#fff" stroke="none"/>
          <circle cx="8" cy="22.5" r="1" fill="#fff" stroke="none"/>
        </svg>
        <span>541-555-0182</span>
      </div>
    </div>
    <div class="email-line">
      <svg width="17" height="12" viewBox="0 0 17 12" fill="none" stroke="#fff" stroke-width="1.4">
        <rect x="0.7" y="0.7" width="15.6" height="10.6"/>
        <path d="M0.7 0.7 L8.5 7 L16.3 0.7"/>
      </svg>
      <span>HELLO@HARLOWPM.COM</span>
    </div>
  </div>
  <div class="back-brand"><span class="brand-dot"></span>HARLOW</div>
  <div class="return-address">218 Cedar Hollow<br>Rd Roseburg, OR 97470</div>
  <div class="stamp-box"></div>
  <div class="address-rule" style="top:233px"></div>
  <div class="address-rule" style="top:272px"></div>
  <div class="address-rule" style="top:310px"></div>
</section>

</body>
</html>
```